Horizon of Bright Tomorrows, LLC needs business stationary designed using our logo.

Horizon of Bright Tomorrows is a new life coaching business. We have a logo design . We need a design for stationary for branding a new PathCrafter Life Coach business. We help people transform their lives by exploring, designing and taking action steps for the life they love in the areas of health and wellness, relationships, vocation, and time and money freedom. We like bright happy colors that present growth and transformation and also compliments the blue logo design.

Hello Designers, Thank you for accepting my design request. I wanted to be sure I put all the information for the business stationary design. If this is already in the order please disregard. Information to incorporate into stationary design Logo: incorporate blues and complimentary color Company name: Horizon of Bright Tomorrows, LLC Tagline: Transformational Life Coaching "If you can think it, you can do it You CAN live a life you LOVE! Website: www.marisolpenwick.PathCrafterGuide.example Email: marisolpenwick@PathCrafterGuide.example P.O. Box 5927 Edcouch, TX 78561 555-317-9042 Marisol T. Penwick, Certified PathCrafter* Coach Positive, upbeat, professional design Thank you.

Industry/Entity Type

Life Coaching

Font styles to use
Decorative

Colors
0355a3

Requirements
Must have
• Information to incorporate into stationary design
• Logo: incorporate blues and complimentary color
• Company name: Horizon of Bright Tomorrows, LLC
• Tagline: Transformational Life Coaching
• "If you can think it, you can do it You CAN live a life you LOVE!
• Website: www.marisolpenwick.PathCrafterGuide.example
• Email: marisolpenwick@PathCrafterGuide.example
• P.O. Box 5927 Edcouch, TX 78561 555-317-9042
• Marisol T. Penwick, Certified PathCrafter* Coach
• Positive, upbeat, professional design
Nice to have
• Watermark
Should not have
• No negativity or negative vibes
• Nothing derogatory
• No clashing colors

```html
<!DOCTYPE html>
<html lang="en">
<head>
<meta charset="utf-8">
<title>Horizon of Bright Tomorrows – Business Cards</title>
<link rel="stylesheet" href="https://fonts.googleapis.com/css2?family=Poppins:wght@300;400;800&family=Roboto+Condensed:wght@400&display=swap">
<style>
  :root {
    --bg: #d6d6da;
    --violet-top: #5e2b98;
    --violet-bottom: #3318c9;
    --brand-blue: #2f17c8;
    --violet: #5a2a9c;
    --ink: #3a3a3a;
    --rule: #c9c9cf;
    --paper: #f6f6f6;
    --silver: #c7c7cc;
  }
  * { margin: 0; padding: 0; box-sizing: border-box; }
  html, body { width: 1200px; height: 972px; overflow: hidden; background: var(--bg); }
  .stage { position: relative; width: 1200px; height: 972px; }

  .card {
    position: absolute; left: 300px; width: 600px; height: 343px;
    border-radius: 20px; overflow: hidden;
    box-shadow: 0 6px 18px rgba(0,0,0,.18);
  }

  /* Back */
  .card-back {
    top: 90px;
    background: linear-gradient(170deg, var(--violet-top) 0%, var(--violet-bottom) 100%);
    color: #fff; text-align: center;
  }
  .card-back .mark-circle {
    position: absolute; left: 50%; top: 62px; width: 110px; height: 110px;
    margin-left: -55px; border-radius: 50%; background: #fff;
  }
  .card-back .company {
    position: absolute; left: 0; right: 0; top: 196px;
    font: 800 27px/1.1 "Poppins", sans-serif; letter-spacing: .2px;
  }
  .card-back .tagline {
    position: absolute; left: 0; right: 0; top: 238px;
    font: 300 17px/1.2 "Poppins", sans-serif; letter-spacing: .6px;
  }

  /* Front */
  .card-front { top: 520px; background: var(--paper); }
  .card-front .wave { position: absolute; left: 0; top: 0; width: 600px; height: 343px; }
  .brand-block {
    position: absolute; left: 34px; top: 52px; width: 230px; text-align: center;
  }
  .brand-block .mark-circle {
    width: 84px; height: 84px; border-radius: 50%; margin: 0 auto 12px;
    background: radial-gradient(circle at 40% 35%, #6a3cc0, var(--violet) 70%);
  }
  .brand-block .company {
    font: 800 17px/1.2 "Poppins", sans-serif; color: var(--brand-blue);
    text-transform: uppercase;
  }
  .divider {
    position: absolute; left: 280px; top: 70px; width: 1px; height: 130px; background: var(--rule);
  }
  .contact { position: absolute; left: 300px; top: 68px; width: 280px; color: var(--ink); }
  .contact .person { font: 800 22px/1.1 "Poppins", sans-serif; color: var(--brand-blue); }
  .contact .role { font: 400 14px/1.3 "Roboto Condensed", sans-serif; margin-bottom: 12px; }
  .contact ul { list-style: none; font: 400 13px/1.6 "Roboto Condensed", sans-serif; }
  .contact li { display: flex; align-items: center; gap: 7px; white-space: nowrap; }
  .contact li svg { width: 12px; height: 12px; flex: none; fill: var(--brand-blue); }
  .contact .address { margin-top: 2px; }
</style>
</head>
<body>
<main class="stage">

  <section class="card card-back" aria-label="Business card back">
    <div class="mark-circle"></div>
    <p class="company">Horizon of Bright Tomorrows, LLC</p>
    <p class="tagline">Transformational Coaching</p>
  </section>

  <section class="card card-front" aria-label="Business card front">
    <svg class="wave" viewBox="0 0 600 343" aria-hidden="true">
      <path d="M0 230 C 150 250, 300 290, 400 343 L 0 343 Z" fill="var(--violet)"/>
      <path d="M0 214 C 150 232, 310 280, 420 343" fill="none" stroke="var(--silver)" stroke-width="14"/>
      <path d="M0 206 C 150 222, 320 272, 432 343" fill="none" stroke="var(--brand-blue)" stroke-width="5"/>
    </svg>

    <div class="brand-block">
      <div class="mark-circle"></div>
      <p class="company">Horizon of Bright<br>Tomorrows, LLC</p>
    </div>

    <div class="divider"></div>

    <div class="contact">
      <p class="person">Marisol T. Penwick</p>
      <p class="role">Certified PathCrafter</p>
      <ul>
        <li><svg viewBox="0 0 24 24"><path d="M6.6 10.8a15 15 0 0 0 6.6 6.6l2.2-2.2a1 1 0 0 1 1-.25 11.4 11.4 0 0 0 3.6.57 1 1 0 0 1 1 1V20a1 1 0 0 1-1 1A17 17 0 0 1 3 4a1 1 0 0 1 1-1h3.5a1 1 0 0 1 1 1c0 1.250.2 2.450.57 3.57a1 1 0 0 1-.25 1z"/></svg>555-317-9042</li>
        <li><svg viewBox="0 0 24 24"><path d="M2 5h20v14H2zM4 7v.5l8 5 8-5V7l-8 5z"/></svg>marisolpenwick@PathCrafterGuide.example</li>
        <li><svg viewBox="0 0 24 24"><path d="M12 2a10 10 0 1 0 0 20 10 10 0 0 0 0-20zm0 2c.9 1.2 1.6 2.5 2 4h-4c.4-1.5 1.1-2.8 2-4zM4.3 14a8 8 0 0 1 0-4h3.3a16 16 0 0 0 0 4zm5.7 0a14 14 0 0 1 0-4h4a14 14 0 0 1 0 4zm6.4 0a16 16 0 0 0 0-4h3.3a8 8 0 0 1 0 4zM10 16h4c-.4 1.5-1.1 2.8-2 4-.9-1.2-1.6-2.5-2-4z"/></svg>www.marisolpenwick.PathCrafterGuide.example</li>
        <li class="address">P.O. Box 5927, Larkmere, TX 78561</li>
      </ul>
    </div>
  </section>

</main>
</body>
</html>
```